Design New Business Card, Envelope and Letter Head !

We need a stationery design for our newly developed logo! We need professional classic look.

Front of the Card:
Logo on the left hand side

Personal Detail in the right hand side
i.e. Name,
Title
Office:
Cell:
Fax:
email:

www.corvelmortgage.example

Color Scheme should match our logo.

Back Side of the Card:

Logo again with Green back ground or off gray back ground ( Note: Color has to be from logo)

and below message. Again, font size and color should come from logo.

" Manifest your trust in us through the gift of your referrals. We won't let you down."
Updates

Dear Designers;

We have updates few info which we missed earlier. Please include those words in the logo and resubmit your designs for consideration.  We are looking for very professional and classic look. Thanks for your great creation. I have changed the payment options. Please have a look and best of luck.

Tobin

Dear All Designers:

For address; please use following address:

" 4719 Copper Glen Ln, San Ramon, CA 94583 " 
Please do not use the address in the website. We would like to give business card with option of calling us is the top priority then email then eFax. Please make sure Put " eFax" in the business card. 

Reason: Since I have updated some information per requirements, I would like to give enough time for the great design work.

Just a note to all designers:

"Equal Opportunity Lender" Sign has to be in back  of the card  in a small image. I would say it has to be "inconspicuous". Let's put the NMLS # and CalBRE # in front side. Let's organise the information follow very elegant and professional.

Requirements
Must have
• We must need following Words in the business card

CalBRE License #

NMLS #

And the logo of " Equal Housing Lender ". Please see the logo attached.

Please put these words or logo represents above at the right location of the card.

```html
<!DOCTYPE html>
<html lang="en">
<head>
<meta charset="utf-8">
<title>Quenby Mortgage – Business Card</title>
<link rel="stylesheet" href="https://fonts.googleapis.com/css2?family=Tinos:wght@400;700&display=swap">
<style>
  :root{
    --bg:#d9d6d1;
    --charcoal:#4a4a4c;
    --card-light:#e7e7e6;
    --green:#3a9a12;
    --ink:#3d3d3f;
    --white:#f4f4f4;
    --badge-red:#c9313a;
  }
  *{box-sizing:border-box;margin:0;padding:0}
  html,body{width:1200px;height:900px;overflow:hidden}
  body{background:var(--bg);font-family:"Tinos","Times New Roman",serif;position:relative;color:var(--ink)}
  .card{position:absolute;width:540px;height:309px;top:296px;box-shadow:0 6px 18px rgba(0,0,0,.18);overflow:hidden}
  .card--back{left:40px;background:var(--charcoal);color:var(--white)}
  .card--front{left:620px;background:var(--card-light)}

  .brand{display:flex;align-items:center;gap:12px}
  .brand__mark{width:26px;height:26px;background:var(--green);flex:none}
  .brand__name{font-size:34px;line-height:1;font-weight:400;letter-spacing:.3px;white-space:nowrap}
  .brand__tagline{font-size:10px;letter-spacing:2.4px;text-transform:uppercase;margin-top:5px;padding-top:4px;border-top:1px solid currentColor;white-space:nowrap}

  .card--back .brand{position:absolute;left:80px;top:78px}
  .card--back .brand__tagline{color:#dcdcdc}
  .back-message{position:absolute;left:0;right:0;top:182px;text-align:center;font-size:17px;line-height:1.45}
  .back-message__pledge{color:var(--green);text-transform:uppercase;letter-spacing:1px}

  .card--front .brand{position:absolute;left:26px;top:128px}
  .card--front .brand__name{font-size:25px;color:var(--ink)}
  .card--front .brand__mark{width:20px;height:20px}
  .card--front .brand__tagline{font-size:7.5px;letter-spacing:1.8px;color:#666}

  .person{position:absolute;left:292px;top:34px}
  .person__name{font-size:23px;line-height:1}
  .person__title{font-size:11px;letter-spacing:1.2px;text-transform:uppercase;margin-top:3px}
  .contact{display:grid;grid-template-columns:44px auto;row-gap:1px;margin-top:12px;font-size:13px}
  .contact dt{color:var(--green)}
  .address{margin-top:12px;font-size:13px;line-height:1.3}
  .website{margin-top:14px;font-size:13px;color:var(--green)}

  .licenses{position:absolute;left:26px;bottom:40px;display:flex;align-items:center;gap:14px;font-size:13px;line-height:1.3}
  .equal-housing{width:36px;height:32px;flex:none}

  .band{position:absolute;left:0;right:0;bottom:0;height:16px;display:flex}
  .band__gray{flex:0 0 60%;background:var(--charcoal)}
  .band__green{flex:1;background:var(--green)}
</style>
</head>
<body>

<section class="card card--back" aria-label="Business card back">
  <div class="brand">
    <span class="brand__mark"></span>
    <div>
      <div class="brand__name">Quenby Mortgage</div>
      <div class="brand__tagline">Your Trusted Mortgage Advisors</div>
    </div>
  </div>
  <p class="back-message">
    Manifest your trust in us through the gift of your referrals.<br>
    <span class="back-message__pledge">We won't let you down.</span>
  </p>
</section>

<section class="card card--front" aria-label="Business card front">
  <div class="brand">
    <span class="brand__mark"></span>
    <div>
      <div class="brand__name">Quenby Mortgage</div>
      <div class="brand__tagline">Your Trusted Mortgage Advisors</div>
    </div>
  </div>

  <div class="person">
    <div class="person__name">Dana Hale</div>
    <div class="person__title">Managing Partner</div>
    <dl class="contact">
      <dt>Office</dt><dd>925.555.0142</dd>
      <dt>Cell</dt><dd>925.555.0187</dd>
      <dt>Fax</dt><dd>925.555.0163</dd>
      <dt>Email</dt><dd>info@quenbymortgage.example</dd>
    </dl>
    <div class="address">4719 Copper Glen Ln,<br>San Ramon, CA 94583</div>
    <div class="website">www.corvelmortgage.example</div>
  </div>

  <div class="licenses">
    <svg class="equal-housing" viewBox="0 0 36 32" role="img" aria-label="Equal housing lender badge">
      <rect x="1" y="1" width="34" height="30" fill="#fff" stroke="var(--badge-red)" stroke-width="1"/>
      <rect x="9" y="7" width="18" height="16" fill="var(--ink)"/>
    </svg>
    <div>CalBRE License # 40718263<br>NMLS # 596032174</div>
  </div>

  <div class="band"><span class="band__gray"></span><span class="band__green"></span></div>
</section>

</body>
</html>
```